Responsive Mobile Lotmo Jewelry Template

We need to adapt an existing Lotmo template to be 100% responsive and mobile friendly. Due to Lotmo rules, the template would need to be implemented only using HTML and CSS (no Javascript). The template design files and HTML/CSS files are required for this project. We prefer that it is implemented using a responsive framework such as Bootstrap.

An example of our current template can be found here (diamond only):
https://www.lotmo.example/itm/510837261904?ViewItem=&item=510837261904

And example of our template with an additional section for gemstone:
https://www.lotmo.example/itm/510837265127?ViewItem=&item=510837265127

We had also somewhat recently designed our Lotmo store landing page so some consistency with this would be desired:
http://www.lotmoshops.example/FernCraftsNY

Please also refer to our website: https://ferncraftsny.example/

Target Market(s)

Primarily women shopping for jewelry on Lotmo.

Industry/Entity Type

Jewelry

Coding

Coded - Design and coding required

Number of Pages Required

1 page

Font styles to use
Sans Serif

Requirements
Must have
• * A color scheme that fits with the existing template design.
• * REMOVE the product photo in the template.
• * Sections required for Description, Basic Details, and Diamond/Gemstone Details.
• * Please refer to https://pages.lotmo.example/sell/itemdescription/mobilefriendlyguidelines.html in particular, the template must use
Nice to have
• * Menu of links to other categories is desired in a mobile friendly way.
• * We are open to graphics for links to popular categories similar to those found on the store page.
• * Implemented using a standardized responsive framework such as Bootstrap.

```html
<!DOCTYPE html>
<html lang="en">
<head>
<meta charset="utf-8">
<title>Fern Crafts New York – Item Template</title>
<link href="https://fonts.googleapis.com/css2?family=Lato:ital,wght@0,400;0,700;1,700&display=swap" rel="stylesheet">
<style>
:root{
  --bg:#ebebeb;
  --sheet:#f4f4f4;
  --card:#ffffff;
  --purple:#a991c6;
  --purple-dark:#8a6bb5;
  --purple-pale:#ece4f7;
  --row-alt:#f4f0fa;
  --line:#dcdcdc;
  --text:#333333;
  --muted:#666666;
  --badge:#d9dde6;
  --badge-dark:#3c5a86;
}
*{box-sizing:border-box;margin:0;padding:0}
html,body{width:670px;height:1200px;overflow:hidden;background:var(--bg);font-family:'Lato',sans-serif;color:var(--text)}
.abs{position:absolute}
.sheet{background:var(--sheet);box-shadow:0 1px 4px rgba(0,0,0,.15)}
.card{background:var(--card);box-shadow:0 0 3px rgba(0,0,0,.12)}
.bar{background:var(--purple);color:#fff;text-align:center;font-weight:700}
.panel{border:1px solid var(--line);background:#fff}
.brand{color:var(--purple-dark);text-align:center;letter-spacing:.5px;display:flex;align-items:center;justify-content:center;gap:5px}
.brand-mark{width:9px;height:9px;background:var(--purple)}
.thumb{background:linear-gradient(135deg,#e3c98e,#c7a8d9);border-radius:50%;flex:none}
.badge{background:var(--badge);border-radius:50%}
.badge.sq{border-radius:2px;background:var(--badge-dark)}
.badge.dark{background:var(--badge-dark)}
table{width:100%;border-collapse:collapse}
td{border-bottom:1px solid var(--line);text-align:center}
td:first-child{border-right:1px solid var(--line)}
tr:nth-child(even) td{background:var(--row-alt)}

/* desktop */
.d-header{left:0;top:0;width:335px;height:33px;background:linear-gradient(var(--purple-pale),#fff);font-size:13px}
.d-nav{top:44px;left:0;width:335px;text-align:center;font-size:6px;font-weight:700}
.d-nav span{margin:0 4px}
.d-desc{left:9px;top:65px;width:316px;height:43px}
.d-desc .bar{height:14px;font-size:7px;line-height:14px}
.d-desc p{font-size:5px;text-align:center;padding:11px 6px;color:var(--muted)}
.d-cats{left:9px;top:119px;width:123px;height:268px}
.d-cats .bar{height:15px;font-size:7.5px;line-height:15px}
.cat{display:flex;align-items:center;height:25.2px;padding:0 6px;border-bottom:1px solid #eee;font-size:5.6px;gap:7px}
.cat:last-child{border:none}
.cat .thumb{width:10px;height:10px}
.cat .name{flex:1;line-height:1.2}
.cat .chev{color:#999;font-size:8px}
.d-details{left:142px;top:119px;width:185px;height:268px}
.d-details .bar{height:16px;font-size:7.5px;line-height:16px}
.d-details td{height:13.6px;font-size:5px;padding:0 5px}
.d-details td:first-child{width:50%}
.note{font-size:5.6px;font-weight:700;font-style:italic;text-align:center;height:18px;line-height:18px}
.ask{font-size:5.5px;font-weight:700;text-align:center;height:25px;line-height:25px}
.ask i{display:inline-block;width:5px;height:4px;background:var(--purple);margin-right:3px}
.d-tabs{left:9px;top:401px;width:317px;height:146px;padding:14px 15px}
.tabs{display:flex;justify-content:center;gap:11px;font-size:5.6px;font-weight:700;margin-bottom:12px}
.tabs .on{color:var(--purple-dark);border-bottom:1px solid var(--purple-dark);padding-bottom:2px}
.ship-lead{color:var(--purple-dark);font-size:5.4px;margin-bottom:5px}
.ship-h{font-size:6.8px;font-weight:700;margin-bottom:7px;letter-spacing:.2px}
.ship p{font-size:4.6px;line-height:1.6;color:var(--muted);margin-bottom:7px}

/* mobile */
.m{font-size:4.3px}
.m .bar{height:11px;line-height:11px;font-size:5.6px}
.m td{font-size:3.8px;padding:1px 2px;height:13px}
.m .cat{height:19.8px;font-size:4.4px;padding:0 4px;gap:4px}
.m .cat .thumb{width:8px;height:8px}
</style>
</head>
<body>

<!-- desktop view -->
<div class="abs sheet" style="left:59px;top:55px;width:410px;height:682px"></div>
<main class="abs card" style="left:97px;top:95px;width:335px;height:602px">
  <div class="abs d-header brand"><span class="brand-mark"></span>FERN CRAFTS NEW YORK</div>
  <nav class="abs d-nav"><span>ABOUT US</span>|<span>FAQS</span>|<span>WHY BUY FROM US</span>|<span>SAVE SELLER</span></nav>

  <section class="abs panel d-desc">
    <div class="bar">Item Description</div>
    <p>Exquisite Oval Aquamarine Gemstone Surrounded By A Delicate Halo Of Diamonds Mounted In A Classic 14k Yellow Gold Setting</p>
  </section>

  <section class="abs panel d-cats">
    <div class="bar">☰&nbsp; Categories</div>
    <div class="cat"><span class="thumb" role="img" aria-label="Engagement ring icon"></span><span class="name">Diamond<br>Engagement Rings</span><span class="chev">›</span></div>
    <div class="cat"><span class="thumb" role="img" aria-label="Fancy yellow ring icon"></span><span class="name">Fancy Yellow &amp;<br>Pink Diamond</span><span class="chev">›</span></div>
    <div class="cat"><span class="thumb" role="img" aria-label="Cocktail ring icon"></span><span class="name">Cocktail Fashion<br>Diamond Rings</span><span class="chev">›</span></div>
    <div class="cat"><span class="thumb" role="img" aria-label="Gemstone ring icon"></span><span class="name">Colored Gemstone<br>Diamond Rings</span><span class="chev">›</span></div>
    <div class="cat"><span class="thumb" role="img" aria-label="Semi mount ring icon"></span><span class="name">Semi Mount<br>Diamond Rings</span><span class="chev">›</span></div>
    <div class="cat"><span class="thumb" role="img" aria-label="Men's ring icon"></span><span class="name">Men's Diamond Jewelry</span><span class="chev">›</span></div>
    <div class="cat"><span class="thumb" role="img" aria-label="Pendant icon"></span><span class="name">Diamond Pendants</span><span class="chev">›</span></div>
    <div class="cat"><span class="thumb" role="img" aria-label="Earrings icon"></span><span class="name">Diamond Earrings</span><span class="chev">›</span></div>
    <div class="cat"><span class="thumb" role="img" aria-label="Necklace icon"></span><span class="name">Diamond Necklaces</span><span class="chev">›</span></div>
    <div class="cat"><span class="thumb" role="img" aria-label="Bracelet icon"></span><span class="name">Diamond Bracelets<br>&amp; Bangles</span><span class="chev">›</span></div>
  </section>

  <section class="abs panel d-details">
    <div class="bar">Item Details</div>
    <table>
      <tr><td>Model Number:</td><td>FCN-RX52817BTK-400</td></tr>
      <tr><td>Metal:</td><td>14k Yellow Gold</td></tr>
      <tr><td>Weight:</td><td>4.08 grams</td></tr>
      <tr><td>L x W x H:</td><td>12 x 10 x 7.2 MM</td></tr>
      <tr><td>Style:</td><td>Halo</td></tr>
      <tr><td>Ring Size:</td><td>6 (contact us for sizing options)</td></tr>
    </table>
    <div class="bar">Diamond Details</div>
    <table>
      <tr><td>Total Carat Weight:</td><td>0.19 CT</td></tr>
      <tr><td>Diamond Count:</td><td>22</td></tr>
      <tr><td>Shape:</td><td>Round</td></tr>
      <tr><td>Color/Clarity:</td><td>G / SI1</td></tr>
      <tr><td>Other Shape:</td><td>Round</td></tr>
      <tr><td>Other Color/Clarity:</td><td>G / SI1</td></tr>
      <tr><td>Certificate:</td><td>GLR (<u style="color:var(--purple-dark)">CLICK FOR MORE INFO</u>)</td></tr>
    </table>
    <div class="note">All of our diamonds and gemstones are 100% natural!</div>
    <div class="bar" style="height:15px;line-height:15px">Questions?</div>
    <div class="ask"><i></i>ASK A QUESTION VIA EMAIL</div>
  </section>

  <section class="abs panel d-tabs ship">
    <div class="tabs"><span class="on">SHIPPING DETAILS</span><span>PRODUCT GUARANTEE</span><span>RETURN POLICY</span><span>PRIVACY POLICY</span><span>WHY US</span></div>
    <div class="ship-lead">ParcelJet 2 Day: Free (U.S.A. only)</div>
    <div class="ship-h">WE SHIP WORLDWIDE</div>
    <p>International Buyers - Please Note: Import duties, taxes, and charges are not included in the item price or shipping cost. These charges are the buyer's responsibility. Please check with your country's customs office to determine what these additional costs will be prior to bidding or buying.</p>
    <p>All packages are fully insured and require signature confirmation.</p>
    <p>Once your item(s) are ready to leave our facility a shipping tracking number will be sent to you. Business days do not include Saturday, Sunday or holidays. Please be sure to inspect your package upon arrival for tampering or any damage. Rush orders are welcome. Please call for availability.</p>
  </section>

  <div class="abs badge sq" style="left:84px;top:558px;width:20px;height:30px"></div>
  <div class="abs badge" style="left:146px;top:564px;width:18px;height:18px"></div>
  <div class="abs badge dark" style="left:210px;top:556px;width:36px;height:36px"></div>
</main>

<!-- mobile view -->
<div class="abs sheet" style="left:517px;top:55px;width:93px;height:1089px"></div>
<aside class="abs card m" style="left:521px;top:65px;width:84px;height:1065px"></aside>
<div class="abs brand" style="left:526px;top:76px;width:75px;font-size:6.5px;background:linear-gradient(var(--purple-pale),#fff);height:16px"><span class="brand-mark" style="width:5px;height:5px"></span>FERN CRAFTS</div>
<div class="abs" style="left:557px;top:96px;width:12px;height:12px;border:1px solid #999;border-radius:50%;font-size:6px;text-align:center;line-height:10px">≡</div>

<section class="abs panel m" style="left:526px;top:120px;width:75px;height:52px">
  <div class="bar">Item Description</div>
  <p style="text-align:center;padding:5px 3px;line-height:1.6;color:var(--muted)">Exquisite Oval Aquamarine Gemstone Surrounded By A Delicate Halo Of Diamonds Mounted In A Classic 14k Yellow Gold Setting</p>
</section>

<section class="abs panel m" style="left:526px;top:183px;width:75px;height:210px">
  <div class="bar">☰ Categories</div>
  <div class="cat"><span class="thumb" role="img" aria-label="Engagement ring icon"></span><span class="name">Diamond<br>Engagement Rings</span></div>
  <div class="cat"><span class="thumb" role="img" aria-label="Fancy yellow ring icon"></span><span class="name">Fancy Yellow &amp;<br>Pink Diamond</span></div>
  <div class="cat"><span class="thumb" role="img" aria-label="Cocktail ring icon"></span><span class="name">Cocktail Fashion<br>Diamond Rings</span></div>
  <div class="cat"><span class="thumb" role="img" aria-label="Gemstone ring icon"></span><span class="name">Colored Gemstone<br>Diamond Rings</span></div>
  <div class="cat"><span class="thumb" role="img" aria-label="Semi mount ring icon"></span><span class="name">Semi Mount<br>Diamond Rings</span></div>
  <div class="cat"><span class="thumb" role="img" aria-label="Men's ring icon"></span><span class="name">Men's Diamond<br>Jewelry</span></div>
  <div class="cat"><span class="thumb" role="img" aria-label="Pendant icon"></span><span class="name">Diamond Pendants</span></div>
  <div class="cat"><span class="thumb" role="img" aria-label="Earrings icon"></span><span class="name">Diamond Earrings</span></div>
  <div class="cat"><span class="thumb" role="img" aria-label="Necklace icon"></span><span class="name">Diamond Necklaces</span></div>
  <div class="cat"><span class="thumb" role="img" aria-label="Bracelet icon"></span><span class="name">Diamond Bracelets<br>&amp; Bangles</span></div>
</section>

<section class="abs panel m" style="left:526px;top:406px;width:75px">
  <div class="bar">Item Details</div>
  <table>
    <tr><td>Model Number:</td><td>FCN-RX52817BTK-400</td></tr>
    <tr><td>Metal:</td><td>14k Yellow Gold</td></tr>
    <tr><td>Weight:</td><td>4.08 grams</td></tr>
    <tr><td>L x W x H:</td><td>12 x 10 x 7.2 MM</td></tr>
    <tr><td>Style:</td><td>Halo</td></tr>
    <tr><td>Ring Size:</td><td>6 (contact us for sizing options)</td></tr>
  </table>
</section>

<section class="abs panel m" style="left:526px;top:514px;width:75px">
  <div class="bar">Diamond Details</div>
  <table>
    <tr><td>Total Carat Weight:</td><td>0.19 CT</td></tr>
    <tr><td>Diamond Count:</td><td>22</td></tr>
    <tr><td>Shape:</td><td>Round</td></tr>
    <tr><td>Color/Clarity:</td><td>G / SI1</td></tr>
    <tr><td>Other Shape:</td><td>Round</td></tr>
    <tr><td>Other Color/Clarity:</td><td>G / SI1</td></tr>
    <tr><td>Certificate:</td><td>GLR<br><i>(click for more info)</i></td></tr>
  </table>
  <div style="font-weight:700;font-style:italic;text-align:center;padding:4px 2px;font-size:4px">All of our diamonds and gemstones are 100% natural!</div>
</section>

<section class="abs panel m" style="left:526px;top:654px;width:75px;height:32px">
  <div class="bar">Questions?</div>
  <div style="font-weight:700;text-align:center;line-height:20px;font-size:4.2px"><i style="display:inline-block;width:4px;height:3px;background:var(--purple);margin-right:2px"></i>ASK A QUESTION VIA EMAIL</div>
</section>

<section class="abs panel m ship" style="left:526px;top:698px;width:75px;height:296px;padding:9px 6px">
  <div style="text-align:center;font-weight:700;line-height:2.2;font-size:4.3px;margin-bottom:6px"><div style="color:var(--purple-dark)">SHIPPING DETAILS</div><div>PRODUCT GUARANTEE</div><div>RETURN POLICY</div><div>PRIVACY POLICY</div><div>WHY US</div></div>
  <div class="ship-lead" style="font-size:4.4px">ParcelJet 2 Day: Free (U.S.A. only)</div>
  <div class="ship-h" style="font-size:5.6px;margin-bottom:5px">WE SHIP WORLDWIDE</div>
  <p style="font-size:3.9px">International Buyers - Please Note: Import duties, taxes, and charges are not included in the item price or shipping cost. These charges are the buyer's responsibility. Please check with your country's customs office to determine what these additional costs will be prior to bidding or buying.</p>
  <p style="font-size:3.9px">All packages are fully insured and require signature confirmation.</p>
  <p style="font-size:3.9px">Once your item(s) are ready to leave our facility a shipping tracking number will be sent to you. Business days do not include Saturday, Sunday or holidays. Please be sure to inspect your package upon arrival for tampering or any damage. Rush orders are welcome. Please call for availability.</p>
</section>

<div class="abs badge" style="left:545px;top:1012px;width:14px;height:14px"></div>
<div class="abs badge dark" style="left:547px;top:1042px;width:32px;height:32px"></div>
<div class="abs badge sq" style="left:545px;top:1086px;width:15px;height:26px"></div>

</body>
</html>
```